Web site for new fundraising service for charities

We need a web design for a new charitable trust based in New Zealand. With the economic downturn, charities are finding it increasingly difficult to raise the monies they need to deliver their services.

Using a network of fundraisers working out of their homes, BrightLot (our charitable trust) will source unique, high interest auction items on behalf of multiple charities - things like luxury cruises, exotic travel, luxury accommodation, fine dining, unique experiences with sports and entertainment personalities, tickets to sporting and entertainment events, etc.

Once we have sourced sufficient high value items we will then partner with Bidora (NZ's equivalent of Vendix) to launch the auction. The proceeds from each auction will benefit up to 6 charities. The auctions will be promoted through Bidora, through PR, and through the communications channels of the benefiting charities, reaching a wider audience than would be possible if just one charity was holding an auction and therefore resulting in more competitive bidding and higher returns for the charities.

We need a web site that we can point potential donors of auction items to, that gives them confidence in BrightLot. We will also leverage the web site with journalists. And of course, charities who are wondering whether or not to use BrightLot will come to our web site and check out our credentials. The tone of the site needs to be warm, friendly, approachable.

We are not locked into the blue and orange colors of the logo and in fact are experimenting with other colors as we speak.

Please note that what we're looking for is the design for the home page, plus a sub page design.

Target Market(s)

CEOs, corporate social responsibility managers, general managers, business owners, charities, the media

Industry/Entity Type

Communications

Requirements
Must have
• Video on home page
Newsletter sign up on all pages
Navigation as per the attached PDF example

```html
<!DOCTYPE html>
<html lang="en">
<head>
<meta charset="utf-8">
<title>BrightLot</title>
<link href="https://fonts.googleapis.com/css2?family=Open+Sans:ital,wght@0,400;0,600;0,700;1,400;1,700&family=Arimo:wght@400&display=swap" rel="stylesheet">
<style>
  :root {
    --peach: #f7e5d8;
    --dark: #33262a;
    --nav: #3d3a3b;
    --brown: #5a4330;
    --brand: #4a1d0f;
    --red: #d01f2e;
    --mauve: #a6707a;
    --text: #3a2a2a;
    --field: #fbf7f4;
    --field-line: #d9cfc8;
    --white: #ffffff;
  }
  * { margin: 0; padding: 0; box-sizing: border-box; }
  html, body { width: 1200px; height: 1000px; overflow: hidden; }
  body { position: relative; background: var(--white); font-family: "Open Sans", sans-serif; color: var(--text); }
  .abs { position: absolute; }

  .hero-photo { left: 0; top: 0; width: 1200px; height: 351px;
    background: linear-gradient(90deg, #f3f1ef 0%, #e9e6e2 35%, #cfcac2 60%, #b8aa9c 80%, #c25a58 100%); }
  .hero-deco { left: 0; top: 0; width: 230px; height: 290px;
    background: linear-gradient(160deg, rgba(170,40,60,.35), rgba(60,60,70,.15) 60%, transparent); }

  .top-links { right: 8px; top: 10px; display: flex; gap: 6px; }
  .top-links a { display: block; height: 47px; width: 125px; text-align: center; line-height: 49px;
    background: rgba(40,32,34,.88); color: var(--white); text-decoration: none; font-size: 15px;
    letter-spacing: 1px; border-radius: 3px; }

  .brand { left: 60px; top: 162px; display: flex; align-items: center; gap: 16px; }
  .brand-mark { width: 86px; height: 86px; border-radius: 50%; background: #f5a000; }
  .brand-name { font-size: 52px; font-weight: 700; color: var(--brand); line-height: 1; letter-spacing: -1px; }

  .main-nav { left: 7px; top: 285px; width: 876px; height: 57px; background: rgba(45,42,43,.9); border-radius: 3px; }
  .main-nav a { position: absolute; top: 20px; color: #f2ece8; text-decoration: none; font-size: 14px; line-height: 18px; }

  .content { left: 0; top: 351px; width: 1200px; height: 519px; background: var(--peach); }
  .icon-swirl { left: 15px; top: 368px; width: 220px; height: 402px;
    background: linear-gradient(160deg, rgba(51,38,42,.15), rgba(51,38,42,.55) 55%, rgba(51,38,42,.2));
    clip-path: polygon(5% 0, 25% 0, 60% 40%, 100% 90%, 95% 100%, 60% 85%, 20% 45%, 0 15%); }

  .intro { left: 233px; top: 392px; }
  .intro .lead { font-size: 15px; color: var(--mauve); line-height: 19px; }
  .intro .ceo { font-size: 15px; color: var(--red); line-height: 19px; }
  .intro .body { font-size: 12.5px; line-height: 15px; color: #2b1d1d; margin-top: 2px; }

  .video { left: 231px; top: 468px; width: 495px; height: 315px; background: var(--brown); }
  .video-frame { left: 7px; top: 6px; width: 482px; height: 271px;
    background: linear-gradient(180deg, #e8d9c3 0%, #d9b58c 55%, #8a7c6e 100%); }
  .video-bar { left: 0; bottom: 0; width: 482px; height: 62px; background: rgba(50,40,40,.75); }
  .play { left: 11px; top: 13px; width: 42px; height: 36px; background: var(--red); border-radius: 2px; }
  .video-actions { left: 6px; top: 284px; display: flex; gap: 7px; }
  .video-actions span { height: 25px; padding: 0 10px; line-height: 25px; color: var(--white); font-size: 13px;
    background: var(--dark); display: flex; align-items: center; gap: 5px; }
  .video-actions .download { background: var(--red); padding: 0 15px 0 10px; }

  .envelope { left: 765px; top: 420px; width: 105px; height: 108px;
    background: linear-gradient(160deg, #eef3f7, #cddbe6); transform: rotate(-12deg); border-radius: 3px; }
  .subscribe { left: 815px; top: 485px; width: 356px; }
  .subscribe h2 { height: 47px; background: var(--dark); color: var(--white); font-style: italic; font-weight: 400;
    font-size: 26px; letter-spacing: 1px; text-align: center; line-height: 48px; border-radius: 3px 3px 0 0; }
  .subscribe .field { display: block; width: 355px; height: 44px; margin: 4px 0 0 1px; background: var(--field);
    border: 1px solid var(--field-line); border-radius: 3px; padding-left: 15px; line-height: 42px;
    font-size: 13px; font-style: italic; letter-spacing: 1px; color: #6d5f5f; }
  .subscribe .field:first-of-type { margin-top: 7px; }
  .submit { left: 1045px; top: 736px; width: 126px; height: 47px; background: var(--dark); color: var(--white);
    font-size: 15px; letter-spacing: 1px; text-align: center; line-height: 52px; border-radius: 3px; }

  .sponsors { left: 162px; top: 834px; width: 876px; height: 57px; background: #474445; border-radius: 3px;
    color: var(--white); font-size: 25px; font-style: italic; text-align: center; line-height: 58px; }
  .sponsors b { font-weight: 700; }

  .footer-deco { left: 948px; top: 870px; width: 252px; height: 130px;
    background: linear-gradient(135deg, rgba(255,255,255,0) 20%, #a11c3a 50%, #2a3340 80%);
    clip-path: polygon(35% 0, 100% 0, 100% 100%, 0 100%); }
  .footer-links { left: 240px; top: 923px; width: 720px; text-align: center; font-family: "Arimo", sans-serif;
    font-size: 10px; letter-spacing: .5px; line-height: 18px; color: #4a4a4a; word-spacing: 2px; }
</style>
</head>
<body>
  <div class="abs hero-photo" role="img" aria-label="Photo of children in a classroom, a boy drawing at a desk"></div>
  <div class="abs hero-deco" role="img" aria-label="Decorative pattern of coloured triangles"></div>

  <nav class="abs top-links">
    <a href="#">DONORS</a><a href="#">CHARITIES</a><a href="#">AUCTIONS</a>
  </nav>

  <div class="abs brand">
    <div class="brand-mark"></div>
    <div class="brand-name">BrightLot</div>
  </div>

  <nav class="abs main-nav">
    <a href="#" style="left:20px">HOME</a>
    <a href="#" style="left:120px">HOW IT WORKS</a>
    <a href="#" style="left:274px">ACTS OF GOODNESS</a>
    <a href="#" style="left:469px">GOODNESS PARTNERS</a>
    <a href="#" style="left:680px">ABOUT</a>
    <a href="#" style="left:789px">CONTACT</a>
  </nav>

  <main class="abs content"></main>
  <div class="abs icon-swirl" role="img" aria-label="Swirl of small charity and health icons"></div>

  <section class="abs intro">
    <p class="lead">This is a fantastic way to raise funds for</p>
    <p class="ceo">Message form CEO</p>
    <p class="body">as it helps privide business with a means<br>of finding new cusomers and contribute to the community same time .</p>
  </section>

  <section class="abs video">
    <div class="abs video-frame" role="img" aria-label="Video still of a runner's legs and shoes at sunrise">
      <div class="abs video-bar">
        <div class="abs play">
          <svg width="42" height="36" viewBox="0 0 42 36"><path d="M16 10 L28 18 L16 26 Z" fill="#fff"/></svg>
        </div>
        <svg class="abs" style="left:66px;top:24px" width="410" height="14" viewBox="0 0 410 14">
          <rect x="0" y="3" width="350" height="8" rx="4" fill="#4a4040"/>
          <rect x="2" y="5" width="114" height="4" rx="2" fill="#2a2020"/>
          <rect x="354" y="1" width="3" height="12" fill="#ccc"/><rect x="359" y="1" width="3" height="12" fill="#ccc"/>
          <rect x="364" y="1" width="3" height="12" fill="#ccc"/><rect x="369" y="1" width="3" height="12" fill="#999"/>
          <rect x="374" y="1" width="3" height="12" fill="#777"/>
          <path d="M388 2 l4 4 M396 2 l-4 4 M388 12 l4 -4 M396 12 l-4 -4" stroke="#ddd" stroke-width="1.5"/>
        </svg>
      </div>
    </div>
    <div class="abs video-actions">
      <span><svg width="12" height="10" viewBox="0 0 12 10"><path d="M1 5 L4.5 8.5 L11 1" stroke="#fff" stroke-width="2" fill="none"/></svg>Follow</span>
      <span><svg width="10" height="10" viewBox="0 0 10 10"><path d="M5 0 V10 M0 5 H10" stroke="#fff" stroke-width="2"/></svg>Share</span>
      <span class="download"><svg width="12" height="14" viewBox="0 0 12 14"><path d="M6 1 V9 M2 6 L6 10 L10 6 M1 13 H11" stroke="#fff" stroke-width="1.5" fill="none"/></svg>Download</span>
    </div>
  </section>

  <div class="abs envelope" role="img" aria-label="Illustration of an envelope with a letter"></div>
  <form class="abs subscribe">
    <h2>SUBSCRIBE NOW</h2>
    <span class="field">FIRST NAME</span>
    <span class="field">LAST NAME</span>
    <span class="field">CITY/TOWN</span>
    <span class="field">EMAIL</span>
  </form>
  <div class="abs submit">SUBMIT</div>

  <div class="abs sponsors">We would like to <b>thanks</b> our&nbsp; <b>Sponcers</b> for their kind <b>Support</b></div>

  <div class="abs footer-deco" role="img" aria-label="Decorative pattern of coloured triangles"></div>
  <footer class="abs footer-links">
    LOREM &nbsp;| &nbsp;IPSUM | SIMPLY &nbsp;| DUMMY &nbsp;| &nbsp;TEXT | THE PRINTING | TYPESETTING | INDUSTRY | LOREM IPSUM | BEEN<br>
    INDUSTRY'S | STANDARD &nbsp;| DUMMY | EVER SINCE | THE 1500S | WHEN | UNKNOWN | PRINTER &nbsp;| TOOK | GALLEY<br>
    ALL RIGHT RESERVED BY BRIGHTLOT
  </footer>
</body>
</html>
```